We are full service plumbing contractors that are capable of performing all of your plumbing need...

A clean, crisp website that conveys we can handle any plumbing from drain cleaning, repairs, to new construction. But emphasis on Leak detection, under-slab and underground water service leaks, repairs, and reroutes. Leak detection by acoustical, Thermal, or tracer gas , methods.Also emphasize advanced drain cleaning technologies and equipment. Don't just poke ahole in the drain blockage, Clean the pipe, with our High pressure hydrojetters, or Chain knocker drain cables that expand to the width of the pipe being cleaned.

Number of Pages Required

5+ page

Font styles to use
Sans Serif

Requirements
Should not have
• Canned photos

```html
<!DOCTYPE html>
<html lang="en">
<head>
<meta charset="utf-8">
<title>Tidewell Plumbing</title>
<link rel="stylesheet" href="https://fonts.googleapis.com/css2?family=Nunito:wght@300;400;600;800;900&display=swap">
<style>
  :root {
    --hero-dark: #2b3240;
    --hero-mid: #5c6470;
    --white: #ffffff;
    --logo-tab: #d9d9d9;
    --brand-blue: #3a72c4;
    --soft-blue: #5b95d1;
    --deep-blue: #2a5590;
    --section-bg: #f1f1f1;
    --heading: #444444;
    --body-text: #2c2c2c;
    --rule: #c9c9c9;
  }
  * { box-sizing: border-box; margin: 0; padding: 0; }
  html, body { width: 1038px; height: 1200px; overflow: hidden; }
  body { font-family: "Nunito", sans-serif; background: var(--section-bg); position: relative; }

  .hero { position: absolute; left: 0; top: 0; width: 1038px; height: 566px; overflow: hidden; }
  .hero-backdrop {
    position: absolute; inset: 0;
    background:
      linear-gradient(180deg, rgba(30,36,50,.85) 0%, rgba(40,46,58,.55) 45%, rgba(50,56,60,.6) 100%),
      linear-gradient(90deg, #6d737a 0%, #8a9096 40%, #7b8288 70%, #4d5a4a 100%);
  }
  .nav-links { position: absolute; top: 35px; left: 0; list-style: none; }
  .nav-links li { position: absolute; color: var(--white); font-size: 12px; white-space: nowrap; }
  .logo-tab {
    position: absolute; left: 457px; top: 0; width: 124px; height: 118px;
    background: var(--logo-tab); border-radius: 0 0 10px 10px;
    display: flex; align-items: center; justify-content: center; gap: 6px;
  }
  .logo-tab .mark { width: 10px; height: 10px; border-radius: 50%; background: var(--brand-blue); }
  .logo-tab .name { font-weight: 800; font-size: 17px; color: var(--brand-blue); }
  .phone { position: absolute; left: 638px; top: 34px; display: flex; align-items: center; gap: 6px; color: var(--white); font-size: 15px; }
  .schedule-btn {
    position: absolute; left: 803px; top: 30px; width: 144px; height: 30px;
    background: var(--brand-blue); color: var(--white); border-radius: 3px;
    font-size: 12px; display: flex; align-items: center; justify-content: center; letter-spacing: .2px;
  }
  .hero-title {
    position: absolute; left: 0; top: 210px; width: 1038px; text-align: center;
    color: var(--white); font-weight: 800; font-size: 37px; line-height: 42px; letter-spacing: -1px;
  }
  .hero-actions { position: absolute; top: 382px; left: 342px; display: flex; gap: 14px; }
  .btn-video {
    width: 159px; height: 43px; border: 1px solid rgba(255,255,255,.55); border-radius: 2px;
    background: rgba(255,255,255,.06); color: var(--white); font-size: 12px;
    display: flex; align-items: center; justify-content: center; gap: 12px;
  }
  .btn-quote {
    width: 181px; height: 43px; background: var(--soft-blue); border-radius: 2px;
    color: var(--white); font-size: 12px; display: flex; align-items: center; justify-content: center;
  }
  .scroll-cue { position: absolute; left: 512px; top: 503px; }

  .about-title {
    position: absolute; top: 608px; left: 0; width: 1038px; text-align: center;
    font-weight: 900; font-size: 37px; color: var(--heading);
  }
  .about-copy { position: absolute; left: 109px; top: 727px; width: 312px; color: var(--body-text); font-size: 16px; line-height: 24.6px; }
  .about-copy p + p { margin-top: 24px; }
  .btn-free {
    position: absolute; left: 109px; top: 1094px; width: 214px; height: 43px;
    background: var(--deep-blue); color: var(--white); border-radius: 3px;
    font-size: 15px; display: flex; align-items: center; justify-content: center;
  }
  .about-photo {
    position: absolute; left: 552px; top: 729px; width: 402px; height: 408px;
    background: linear-gradient(135deg, #8a8580 0%, #b7b3ab 40%, #6f6a62 75%, #4e4a44 100%);
  }
  .section-rule { position: absolute; left: 166px; top: 1173px; width: 677px; height: 1px; background: var(--rule); }
</style>
</head>
<body>
  <header class="hero">
    <div class="hero-backdrop" role="img" aria-label="Company service vans parked on a driveway under palm trees"></div>
    <ul class="nav-links">
      <li style="left:116px">Who we are</li>
      <li style="left:213px">Plumbing</li>
      <li style="left:295px">Heating</li>
      <li style="left:369px">Services</li>
    </ul>
    <div class="logo-tab"><span class="mark"></span><span class="name">Tidewell</span></div>
    <div class="phone">
      <svg width="14" height="16" viewBox="0 0 14 16" fill="none" stroke="#fff" stroke-width="1.2"><path d="M3 1h2.5l1.2 3.5-1.8 1.2a8 8 0 0 0 4.4 5l1.3-1.7L14 10.2V13c0 1-1 2-2 2C6 14.6 1 9.5 1 3.2 1 2 2 1 3 1z"/></svg>
      <span>9400 555 018</span>
    </div>
    <div class="schedule-btn">SCHEDULE SERVICE</div>
    <h1 class="hero-title">We are a team of highly trained<br>plumbers with respect for<br>your home.</h1>
    <div class="hero-actions">
      <div class="btn-video">
        <svg width="10" height="12" viewBox="0 0 10 12"><path d="M0 0l10 6-10 6z" fill="#fff"/></svg>
        <span>Watch video</span>
      </div>
      <div class="btn-quote">Get a free quote from us</div>
    </div>
    <svg class="scroll-cue" width="14" height="20" viewBox="0 0 14 20"><rect x="1" y="1" width="12" height="18" rx="6" fill="none" stroke="rgba(255,255,255,.7)" stroke-width="1.2"/><circle cx="7" cy="7" r="1.4" fill="#fff"/></svg>
  </header>

  <section class="about">
    <h2 class="about-title">Who we are</h2>
    <div class="about-copy">
      <p>At Tidewell, we know it can be frustrating for customers who have previously been over charged or let down by their local plumbers. We can show you that not all plumbing, boiler and heating companies are the same. We value our customers and always put them first!</p>
      <p>We have a great customer return rate and we constantly strive to increase this. If your looking for the best plumbing, boiler or heating services. Give us a try!</p>
    </div>
    <div class="btn-free">GET A FREE QUOTE</div>
    <div class="about-photo" role="img" aria-label="Plumber crouching under a house repairing a drain pipe"></div>
    <div class="section-rule"></div>
  </section>
</body>
</html>
```